Business Advisory Firm Business Card

A clean, very upscale looking business card. Not crowded.

Please include logo (attached) and:

Daria K. Pellworth
Four Marlow Court
New York, NY 10023
tel: (917) 555-0143
fax: (646) 555-0172
email: dpellworth@quarrystoneconsultants.example
website: www.quarrystoneconsultants.example

Target Market(s)

Business clients. Often real estate development firms, other advisory firms or growing companies that need assistance. I would like a card that looks impressive and confident.

Industry/Entity Type

Business

Colors

Designer to choose colors to be used in the design.

Requirements
Must have
• Impressive and confident. Please include logo.
Should not have
• nothing flashy...

```html
<!DOCTYPE html>
<html lang="en">
<head>
<meta charset="utf-8">
<title>Quarrystone Advisory Services – Business Card</title>
<link rel="stylesheet" href="https://fonts.googleapis.com/css2?family=Oswald:wght@300;400&display=swap">
<style>
  :root {
    --canvas: #ececea;
    --paper: #ffffff;
    --lime: #a6cf38;
    --lime-deep: #6f8f1f;
    --ink: #2b2b2b;
    --grey: #5c5c5c;
    --mark: #8a8a8a;
  }
  * { box-sizing: border-box; margin: 0; padding: 0; }
  html, body {
    width: 1200px;
    height: 800px;
    overflow: hidden;
    background: var(--canvas);
    font-family: "Oswald", "Arial Narrow", sans-serif;
  }
  .sheet {
    position: relative;
    width: 1200px;
    height: 800px;
  }
  .card {
    position: absolute;
    top: 257px;
    width: 500px;
    height: 286px;
    background: var(--paper);
    box-shadow: 0 6px 20px rgba(0,0,0,0.12);
    overflow: hidden;
  }
  .card--front { left: 67px; }
  .card--back { left: 633px; }

  /* Front */
  .front__header {
    position: absolute;
    top: 0; left: 0; right: 0;
    height: 116px;
    padding: 38px 34px 0 34px;
    text-align: right;
    text-transform: uppercase;
  }
  .front__name {
    color: var(--lime);
    font-weight: 400;
    font-size: 22px;
    line-height: 1.1;
    letter-spacing: 0.2px;
  }
  .front__address {
    color: var(--grey);
    font-weight: 300;
    font-size: 15px;
    line-height: 1.2;
  }
  .front__address .city { color: #8c8c8c; }
  .front__rule {
    position: absolute;
    top: 116px; left: 0; right: 0;
    height: 4px;
    background: var(--lime-deep);
  }
  .front__band {
    position: absolute;
    top: 120px; left: 0; right: 0; bottom: 0;
    background: var(--lime);
    padding: 46px 30px 0 30px;
    color: var(--paper);
    text-transform: uppercase;
  }
  .contact-list { list-style: none; }
  .contact-list li {
    font-weight: 400;
    font-size: 14px;
    line-height: 1.35;
    letter-spacing: 0.1px;
  }

  /* Back */
  .back__brand {
    position: absolute;
    inset: 0;
    display: flex;
    flex-direction: column;
    align-items: center;
    justify-content: center;
    gap: 16px;
  }
  .back__square {
    width: 44px;
    height: 44px;
    background: var(--mark);
  }
  .back__name {
    color: var(--ink);
    font-weight: 400;
    font-size: 24px;
    font-variant: small-caps;
    letter-spacing: 0.3px;
  }
</style>
</head>
<body>
<main class="sheet">
  <section class="card card--front" aria-label="Business card front">
    <header class="front__header">
      <h1 class="front__name">Daria K. Pellworth</h1>
      <p class="front__address">Four Marlow Court <span class="city">New York, NY 10023</span></p>
    </header>
    <div class="front__rule"></div>
    <div class="front__band">
      <ul class="contact-list">
        <li>Tel: (917) 555-0143</li>
        <li>Fax: (646) 555-0172</li>
        <li>Email: dpellworth@quarrystoneconsultants.example</li>
        <li>Website: www.quarrystoneconsultants.example</li>
      </ul>
    </div>
  </section>

  <section class="card card--back" aria-label="Business card back">
    <div class="back__brand">
      <div class="back__square"></div>
      <p class="back__name">Quarrystone Advisory Services, Inc.</p>
    </div>
  </section>
</main>
</body>
</html>
```